Boutique Technology Consultancy specialising is Electronic and physical security

We need to redo our existing outdated website. For your reference the link www.brivo.com.au

```html
<!DOCTYPE html>
<html lang="en">
<head>
<meta charset="utf-8">
<title>Orvelt Services — Technology Consultancy</title>
<link href="https://fonts.googleapis.com/css2?family=Lexend:wght@300;400;500;600&display=swap" rel="stylesheet">
<style>
:root{
  --red:#b3161c;
  --red-deep:#6b0f12;
  --ink:#1c1c1c;
  --muted:#555;
  --dark:#150708;
  --line:#d9d9d9;
  --white:#fff;
}
*{box-sizing:border-box;margin:0;padding:0}
html,body{width:1200px;height:4781px;overflow:hidden}
body{position:relative;background:var(--white);font-family:'Lexend',sans-serif;color:var(--ink)}
.abs{position:absolute}
a{color:inherit;text-decoration:none}

.sidebar{left:0;top:0;width:117px;height:4781px;background:var(--white)}
.menu-icon{left:44px;top:22px}
.menu-label{left:44px;top:70px;font-size:11px;color:var(--ink)}
.side-social{left:41px;width:37px;height:37px;border-radius:50%;background:var(--red);display:flex;align-items:center;justify-content:center}
.read-tab{left:40px;top:531px;width:36px;height:159px;background:linear-gradient(var(--red),var(--red-deep));color:#fff;font-size:10px;font-weight:500;writing-mode:vertical-rl;display:flex;align-items:center;justify-content:center;border-bottom:4px double var(--red)}

.brand{display:flex;align-items:center;gap:8px}
.brand-mark{width:24px;height:24px;border-radius:50%;background:var(--red)}
.brand-name{font-size:32px;font-weight:500;color:var(--red-deep);letter-spacing:1px}
.contact-item{display:flex;align-items:center;gap:14px}
.contact-icon{width:37px;height:37px;border-radius:50%;background:var(--red);display:flex;align-items:center;justify-content:center}
.contact-item small{display:block;font-size:10px;color:#777}
.contact-item span{font-size:11.5px;font-weight:500}
.divider-v{width:1px;height:24px;background:#bbb;top:24px}

.hero{left:117px;top:75px;width:1083px;height:595px;background:linear-gradient(120deg,#2b2b2d,#4a4a4c 45%,#232324);overflow:hidden}
.hero-overlay{inset:0;background:linear-gradient(180deg,rgba(0,0,0,.25),rgba(0,0,0,.45))}
.eyebrow{display:flex;align-items:center;justify-content:center;gap:26px;font-size:14px;font-weight:500}
.eyebrow i{display:block;width:56px;height:2px;background:currentColor}
.hero-eyebrow{left:0;right:0;top:265px;color:#fff}
.hero-title{left:0;right:0;top:288px;text-align:center;color:#fff;font-size:60px;font-weight:400;line-height:70px;letter-spacing:-1px}
.dots{display:flex;gap:16px;align-items:center}
.dot{width:10px;height:10px;border-radius:50%;background:#fff}
.dot.active{width:20px;height:20px;border:1px solid #fff;background:transparent;display:flex;align-items:center;justify-content:center}
.dot.active::after{content:"";width:8px;height:8px;border-radius:50%;background:#fff}

.label{display:flex;align-items:center;gap:30px;font-size:14px;font-weight:500;color:var(--red-deep)}
.label i{display:block;width:60px;height:2px;background:var(--red)}
.h2{font-size:40px;font-weight:400;line-height:46px;letter-spacing:-.6px;color:var(--ink)}
.body-text{font-size:11.5px;line-height:24px;color:var(--muted)}

.tabs{left:166px;top:918px;display:flex;gap:15px}
.tab{width:94px;height:34px;border:1px solid var(--red-deep);font-size:10.5px;display:flex;align-items:center;justify-content:center;color:var(--ink)}
.tab.on{background:var(--red-deep);color:#fff}
.checks{left:166px;top:1105px;display:grid;grid-template-columns:168px 200px;row-gap:18px;font-size:11px}
.checks li{list-style:none;display:flex;align-items:center;gap:12px}
.btn-red{background:linear-gradient(90deg,var(--red-deep),var(--red));color:#fff;font-size:11px;font-weight:500;display:flex;align-items:center;justify-content:center;gap:14px;border-right:6px double #e24b4f}
.badge{left:511px;top:1274px;width:218px;height:63px;background:var(--red);border:2px dashed #fff;outline:3px solid var(--red);display:flex;align-items:center;gap:14px;padding-left:28px;color:#fff;font-size:11px}

.band{left:117px;width:1083px;background:radial-gradient(ellipse at 80% 90%,#7a1014 0%,#3a0709 40%,#150708 80%)}
.band-eyebrow{color:#fff;left:0;right:0}
.band-title{left:0;right:0;text-align:center;color:#fff;font-size:40px;font-weight:400;letter-spacing:-.6px}
.band-desc{left:0;right:0;text-align:center;color:#eee;font-size:11.5px;line-height:24px}
.svc-card{background:rgba(255,255,255,.12);color:#fff;display:flex;flex-direction:column;align-items:center;justify-content:center;gap:14px;text-align:center}
.svc-card h3{font-size:22px;font-weight:400;line-height:28px}
.svc-card p{font-size:9.5px;line-height:20px;color:#ddd}
.round-arrow{width:38px;height:38px;border-radius:50%;background:#fff;display:flex;align-items:center;justify-content:center}
.btn-white{background:#fff;color:var(--ink);font-size:11px;font-weight:500;display:flex;align-items:center;justify-content:center;gap:14px;border-right:6px double #fff}

.skill-name{font-size:11.5px;color:var(--ink)}
.skill-pct{font-size:14px;color:var(--red)}
.track{height:2px;background:var(--line)}
.fill{height:2px;background:var(--red)}
.knob{width:11px;height:11px;border-radius:50%;background:var(--red-deep);top:-5px}

.team-card{width:262px;height:308px;background:linear-gradient(180deg,#3b3b3b,#1e1e1e)}
.team-card.b{background:linear-gradient(180deg,#5a4a40,#2b2622)}
.team-bio{left:0;right:0;bottom:28px;text-align:center;color:#fff;font-size:9.5px;line-height:20px;padding:0 30px}
.team-social{display:flex;gap:8px;justify-content:center;margin-top:14px}
.team-social span{width:20px;height:20px;border-radius:50%;background:#fff}
.member{width:262px;text-align:center;color:#fff}
.member h4{font-size:17px;font-weight:500}
.member p{font-size:12px;margin-top:14px;color:#eee}

.post{width:279px;height:290px;background:linear-gradient(160deg,#8d8f96,#3f4450)}
.post-date{right:0;top:0;width:58px;height:64px;background:#fff;color:var(--red);font-size:11px;text-align:center;padding-top:14px;line-height:15px}
.post-title{left:30px;bottom:36px;color:#fff;font-size:15px;line-height:20px}

.footer h5{font-size:20px;font-weight:400;color:#fff}
.quick-links{right:855px;top:4470px;text-align:right;list-style:none;color:#fff;font-size:13px;line-height:36.5px}
.f-social{width:36px;height:36px;border-radius:50%;background:#fff;display:flex;align-items:center;justify-content:center}
.f-social.on{background:var(--red)}
.f-contact{display:flex;gap:18px;color:#fff;font-size:13px;line-height:24px;width:260px}
.f-contact .ic{flex:none;width:40px;height:40px;border-radius:50%;background:#fff;display:flex;align-items:center;justify-content:center}
</style>
</head>
<body>

<aside class="abs sidebar">
  <svg class="abs menu-icon" width="34" height="28" viewBox="0 0 34 28"><rect y="0" width="34" height="4" rx="2" fill="#b3161c"/><rect y="11" width="26" height="4" rx="2" fill="#b3161c"/><rect y="22" width="18" height="4" rx="2" fill="#b3161c"/></svg>
  <div class="abs menu-label">Menu</div>
  <div class="abs side-social" style="top:190px"><svg width="12" height="12"><circle cx="6" cy="6" r="3" fill="#fff"/></svg></div>
  <div class="abs side-social" style="top:241px"><svg width="12" height="12"><circle cx="6" cy="6" r="3" fill="#fff"/></svg></div>
  <div class="abs side-social" style="top:292px"><svg width="12" height="12"><circle cx="6" cy="6" r="3" fill="#fff"/></svg></div>
  <div class="abs side-social" style="top:343px"><svg width="12" height="12"><circle cx="6" cy="6" r="3" fill="#fff"/></svg></div>
  <div class="abs side-social" style="top:394px"><svg width="12" height="12"><circle cx="6" cy="6" r="3" fill="#fff"/></svg></div>
  <div class="abs read-tab">Read More →</div>
</aside>

<header>
  <div class="abs brand" style="left:128px;top:18px"><span class="brand-mark"></span><span class="brand-name">ORVELT</span></div>
  <div class="abs contact-item" style="left:406px;top:19px">
    <span class="contact-icon"><svg width="14" height="18" viewBox="0 0 14 18"><path d="M7 0a7 7 0 0 0-7 7c0 5 7 11 7 11s7-6 7-11a7 7 0 0 0-7-7zm0 10a3 3 0 1 1 0-6 3 3 0 0 1 0 6z" fill="#fff"/></svg></span>
    <div><small>Our Location</small><span>Melbourne Vic 3005</span></div>
  </div>
  <div class="abs divider-v" style="left:624px"></div>
  <div class="abs contact-item" style="left:673px;top:19px">
    <span class="contact-icon"><svg width="16" height="16" viewBox="0 0 24 24"><path d="M6.6 10.8a15 15 0 0 0 6.6 6.6l2.2-2.2c.3-.3.7-.4 1-.2 1.1.4 2.3.6 3.6.6.6 0 1 .4 1 1V20c0 .6-.4 1-1 1A17 17 0 0 1 3 4c0-.6.4-1 1-1h3.5c.6 0 1 .4 1 1 0 1.3.2 2.5.6 3.6.1.3 0 .7-.2 1z" fill="#fff"/></svg></span>
    <div><small>Call Us On</small><span>1300 555 014</span></div>
  </div>
  <div class="abs divider-v" style="left:855px"></div>
  <div class="abs contact-item" style="left:903px;top:19px">
    <span class="contact-icon"><svg width="16" height="12" viewBox="0 0 16 12"><rect width="16" height="12" rx="1" fill="#fff"/><path d="M0 1l8 6 8-6" stroke="#b3161c" stroke-width="1.5" fill="none"/></svg></span>
    <div><small>Email Us On</small><span>hello@orvelt.com.au</span></div>
  </div>
</header>

<section class="abs hero" role="img" aria-label="Business people in suits reviewing charts and documents at a meeting table">
  <div class="abs hero-overlay"></div>
  <div class="abs eyebrow hero-eyebrow"><i></i>Orvelt Services<i></i></div>
  <h1 class="abs hero-title">Your Technology<br>Projects Made Easy</h1>
  <div class="abs dots" style="left:504px;top:504px"><span class="dot active"></span><span class="dot"></span><span class="dot"></span></div>
</section>

<section class="about">
  <div class="abs label" style="left:166px;top:783px"><i></i>About Our Company</div>
  <h2 class="abs h2" style="left:166px;top:810px">Transforming Visions<br>into Tech Realities</h2>
  <div class="abs tabs"><span class="tab on">About Us</span><span class="tab">Our Mission</span><span class="tab">Vision</span></div>
  <p class="abs body-text" style="left:166px;top:970px;width:360px">Orvelt Is A Privately Owned Independent Consultancy 100% Dedicated To Customer Satisfaction. With Experience In A Range Of Technologies Such As Internet Of Things, Security Systems, Wi-Fi, Building Services Networks, Control Centres And Smart Buildings, Our Services Include:</p>
  <ul class="abs checks">
    <li><svg width="14" height="14"><circle cx="7" cy="7" r="6" stroke="#b3161c" fill="none"/><path d="M4 7l2 2 4-4" stroke="#b3161c" fill="none"/></svg>Technology Audits</li>
    <li><svg width="14" height="14"><circle cx="7" cy="7" r="6" stroke="#b3161c" fill="none"/><path d="M4 7l2 2 4-4" stroke="#b3161c" fill="none"/></svg>Technology Roadmaps</li>
    <li><svg width="14" height="14"><circle cx="7" cy="7" r="6" stroke="#b3161c" fill="none"/><path d="M4 7l2 2 4-4" stroke="#b3161c" fill="none"/></svg>Technology Designs</li>
    <li><svg width="14" height="14"><circle cx="7" cy="7" r="6" stroke="#b3161c" fill="none"/><path d="M4 7l2 2 4-4" stroke="#b3161c" fill="none"/></svg>Technology Procurement</li>
    <li style="grid-column:1/3"><svg width="14" height="14"><circle cx="7" cy="7" r="6" stroke="#b3161c" fill="none"/><path d="M4 7l2 2 4-4" stroke="#b3161c" fill="none"/></svg>Technology Project Management</li>
  </ul>
  <a class="abs btn-red" style="left:166px;top:1248px;width:160px;height:38px">Read More <span>⟶</span></a>
  <div class="abs" style="left:614px;top:783px;width:470px;height:555px;background:linear-gradient(160deg,#c9cdd2,#8a8f96 60%,#4a4c52)" role="img" aria-label="Two colleagues in business attire reviewing a tablet in a bright office"></div>
  <div class="abs badge"><svg width="22" height="24" viewBox="0 0 22 24"><circle cx="11" cy="9" r="8" stroke="#fff" stroke-width="2" fill="none"/><path d="M6 15l-2 8 7-3 7 3-2-8" stroke="#fff" stroke-width="2" fill="none"/></svg>10+ Year In Industry</div>
</section>

<section class="abs band" style="top:1450px;height:768px">
  <div class="abs eyebrow band-eyebrow" style="top:110px"><i></i>Our Services<i></i></div>
  <h2 class="abs band-title" style="top:136px">Innovate with Confidence</h2>
  <p class="abs band-desc" style="top:192px;padding:0 210px">Orvelt Services Provides Independent Professional Services For Projects As Well As Operations And Maintenance. We Offer End To End Services Including:</p>
  <div class="abs svc-card" style="left:119px;top:310px;width:265px;height:232px">
    <svg width="48" height="48" viewBox="0 0 48 48"><rect x="6" y="22" width="6" height="18" fill="#fff"/><rect x="16" y="14" width="6" height="26" fill="#fff"/><rect x="26" y="18" width="6" height="22" fill="#fff"/><circle cx="34" cy="32" r="7" stroke="#fff" stroke-width="3" fill="none"/><path d="M39 37l6 6" stroke="#fff" stroke-width="3"/></svg>
    <h3>Strategy</h3>
  </div>
  <div class="abs svc-card" style="left:410px;top:275px;width:265px;height:302px">
    <svg width="52" height="52" viewBox="0 0 52 52"><circle cx="20" cy="32" r="10" stroke="#fff" stroke-width="4" fill="none"/><rect x="30" y="12" width="5" height="14" fill="#fff"/><rect x="38" y="6" width="5" height="20" fill="#fff"/><rect x="22" y="16" width="5" height="6" fill="#fff"/></svg>
    <h3>Operations and<br>maintenance</h3>
    <p>Lorem Ipsum Is Simply Dummy Text<br>Of The Printing</p>
    <span class="round-arrow"><svg width="12" height="12"><path d="M2 10L10 2M4 2h6v6" stroke="#1c1c1c" fill="none"/></svg></span>
  </div>
  <div class="abs svc-card" style="left:701px;top:310px;width:265px;height:232px">
    <svg width="48" height="48" viewBox="0 0 48 48"><circle cx="16" cy="24" r="11" stroke="#fff" stroke-width="4" fill="none"/><rect x="22" y="12" width="20" height="24" rx="2" fill="#fff"/><path d="M26 18h12M26 24h12M26 30h12" stroke="#3a0709" stroke-width="2"/></svg>
    <h3>Projects</h3>
  </div>
  <a class="abs btn-white" style="left:464px;top:618px;width:158px;height:35px">View All <span>⟶</span></a>
</section>

<section class="why">
  <div class="abs" style="left:166px;top:2330px;width:474px;height:555px;background:linear-gradient(150deg,#5b5f66,#9a8f86 50%,#3c3e43)" role="img" aria-label="Smiling professionals shaking hands in an office with a laptop on the desk"></div>
  <span class="abs" style="left:366px;top:2572px;width:72px;height:72px;border-radius:50%;background:#fff;display:flex;align-items:center;justify-content:center"><svg width="20" height="22"><path d="M3 1l16 10L3 21z" fill="#1c1c1c"/></svg></span>
  <div class="abs label" style="left:692px;top:2392px"><i></i>Why Choose Us</div>
  <h2 class="abs h2" style="left:692px;top:2420px">Tech Excellence,<br>Strategic Brilliance</h2>
  <p class="abs body-text" style="left:692px;top:2518px;width:390px;line-height:22.5px">Lorem Ipsum is simply dummy text of the printing and typesetting industry. Lorem Ipsum has been the industry's standard dummy text ever since the 1500s,</p>
  <p class="abs body-text" style="left:692px;top:2608px;width:390px;line-height:22.5px">Lorem ipsum is simply dummy text of the printing and typesetting industry.</p>

  <span class="abs skill-name" style="left:692px;top:2678px">Property/Facilities Management</span><span class="abs skill-pct" style="left:952px;top:2675px">75%</span>
  <div class="abs track" style="left:692px;top:2708px;width:388px"><div class="fill" style="width:281px"></div><span class="abs knob" style="left:276px"></span></div>
  <span class="abs skill-name" style="left:692px;top:2733px">Asset Management</span><span class="abs skill-pct" style="left:1000px;top:2730px">85%</span>
  <div class="abs track" style="left:692px;top:2763px;width:388px"><div class="fill" style="width:328px"></div><span class="abs knob" style="left:323px"></span></div>
  <span class="abs skill-name" style="left:692px;top:2788px">Development And Construction</span><span class="abs skill-pct" style="left:1022px;top:2785px">90%</span>
  <div class="abs track" style="left:692px;top:2818px;width:388px"><div class="fill" style="width:349px"></div><span class="abs knob" style="left:344px"></span></div>
</section>

<section class="abs band" style="top:2998px;height:772px;background:radial-gradient(ellipse at 20% 50%,#7a1014 0%,#3a0709 45%,#150708 85%)">
  <div class="abs eyebrow band-eyebrow" style="top:110px"><i></i>Our Team<i></i></div>
  <h2 class="abs band-title" style="top:134px">Your Formula for Business Success</h2>
  <div class="abs team-card" style="left:123px;top:224px" role="img" aria-label="Portrait of a principal consultant">
    <div class="abs team-bio">Adrian founded Norvale Group in 2016 and joined Orvelt as a Director in 2022, taking over leadership of the NSW office.
      <div class="team-social"><span></span><span></span><span></span><span></span></div></div>
  </div>
  <div class="abs team-card b" style="left:412px;top:224px" role="img" aria-label="Portrait of a principal consultant"></div>
  <div class="abs team-card b" style="left:701px;top:224px" role="img" aria-label="Portrait of a senior consultant"></div>
  <div class="abs member" style="left:123px;top:556px"><h4>ADRIAN VALE</h4><p>Principal Consultant</p></div>
  <div class="abs member" style="left:412px;top:556px"><h4>MARTIN COLES</h4><p>Principal Consultant</p></div>
  <div class="abs member" style="left:701px;top:556px"><h4>PETER HENSLEY</h4><p>Senior Consultant</p></div>
  <div class="abs dots" style="left:504px;top:638px"><span class="dot active"></span><span class="dot"></span><span class="dot"></span></div>
</section>

<section class="blog">
  <div class="abs label" style="left:166px;top:3882px"><i></i>Latest News &amp; Blog</div>
  <h2 class="abs h2" style="left:166px;top:3908px">Read Our Latest<br>Articles</h2>
  <p class="abs body-text" style="left:166px;top:4012px;width:290px;line-height:26px">Lorem Ipsum is simply dummy text of the printing and typesetting industry. Lorem Ipsum has been the industry's standard dummy text ever since the 1500s, when an unknown printer took a galley of type and scrambled it to make a type specimen book.</p>
  <article class="abs post" style="left:498px;top:3905px" role="img" aria-label="Business team discussing documents in an office">
    <div class="abs post-date">22-Nov<br>2023</div>
    <div class="abs post-title">Lorem Ipsum is simply<br>dummy text of the</div>
  </article>
  <article class="abs post" style="left:802px;top:3905px" role="img" aria-label="Colleagues reviewing a tablet together">
    <div class="abs post-date">22-Aug<br>2023</div>
    <div class="abs post-title">Lorem Ipsum is simply<br>dummy text of the</div>
  </article>
</section>

<footer class="abs band footer" style="top:4310px;height:471px;background:radial-gradient(ellipse at 85% 70%,#8a1217 0%,#3a0709 45%,#150708 85%)">
  <h5 class="abs" style="left:116px;top:114px">Quick Links</h5>
  <div class="abs brand" style="left:410px;top:122px"><span class="brand-mark" style="background:#fff"></span><span class="brand-name" style="color:#fff">ORVELT</span></div>
  <div class="abs" style="left:405px;top:217px;display:flex;gap:14px">
    <span class="f-social on"></span><span class="f-social"></span><span class="f-social"></span><span class="f-social"></span>
  </div>
  <p class="abs" style="left:0;width:1083px;text-align:center;top:308px;color:#ddd;font-size:12px">© Copyright 2023 <b style="color:#fff;font-weight:500">Orvelt Services</b> . All rights reserved</p>
  <p class="abs" style="left:0;width:1083px;text-align:center;top:336px;color:#fff;font-size:12px;font-weight:500">Privacy Policy &nbsp;|&nbsp; Sitemap</p>
  <h5 class="abs" style="left:770px;top:114px">Contact Us</h5>
  <div class="abs f-contact" style="left:770px;top:160px"><span class="ic"><svg width="12" height="16" viewBox="0 0 14 18"><path d="M7 0a7 7 0 0 0-7 7c0 5 7 11 7 11s7-6 7-11a7 7 0 0 0-7-7zm0 10a3 3 0 1 1 0-6 3 3 0 0 1 0 6z" fill="#6b0f12"/></svg></span><span>Level 2, 88 Harbour Lane, Melbourne VIC 3005</span></div>
  <div class="abs f-contact" style="left:770px;top:258px;align-items:center"><span class="ic"><svg width="14" height="14"><path d="M1 7L13 1 9 13 7 8z" fill="#6b0f12"/></svg></span><span>hello@orvelt.com.au</span></div>
  <div class="abs f-contact" style="left:770px;top:322px;align-items:center"><span class="ic"><svg width="14" height="14" viewBox="0 0 24 24"><path d="M6.6 10.8a15 15 0 0 0 6.6 6.6l2.2-2.2c.3-.3.7-.4 1-.2 1.1.4 2.3.6 3.6.6.6 0 1 .4 1 1V20c0 .6-.4 1-1 1A17 17 0 0 1 3 4c0-.6.4-1 1-1h3.5c.6 0 1 .4 1 1 0 1.3.2 2.5.6 3.6.1.3 0 .7-.2 1z" fill="#6b0f12"/></svg></span><span>1300 555 014</span></div>
</footer>
<ul class="abs quick-links">
  <li>Home</li><li>About Us</li><li>Our Services</li><li>Experience</li><li>Our Team</li><li>Contact Us</li>
</ul>

</body>
</html>
```